Business Card Design Project

Financial planning, Insurance and Real estate - Financial Services company

Contact Information for Business Card

Looking for something simple in design -
Tolverin Equity LLC
Tolverin Wealth Managment

```html
<!DOCTYPE html>
<html lang="en">
<head>
<meta charset="utf-8">
<title>Tolverin Wealth Management – Business Card</title>
<link rel="stylesheet" href="https://fonts.googleapis.com/css2?family=Anton&family=Exo+2:wght@400;600;700&display=swap">
<style>
  :root {
    --backdrop: #2a2c30;
    --card: #111214;
    --card-edge: #1c1d20;
    --brand-blue: #1a86d0;
    --ink-light: #f2f4f6;
    --ink-muted: #c9ccd1;
    --ink-dark: #101114;
  }
  * { box-sizing: border-box; margin: 0; padding: 0; }
  html, body {
    width: 1200px; height: 900px; overflow: hidden;
    background: var(--backdrop);
  }
  .canvas {
    position: relative; width: 1200px; height: 900px;
    display: flex; align-items: center; justify-content: center; gap: 60px;
  }
  .card {
    position: relative; width: 510px; height: 292px;
    background: var(--card);
    border: 1px solid var(--card-edge);
    border-radius: 4px;
    box-shadow: 0 12px 30px rgba(0,0,0,.45);
    overflow: hidden;
  }
  .brand-dot {
    display: block; border: 3px solid var(--brand-blue); border-radius: 50%;
  }

  /* Front */
  .front .brand-dot { position: absolute; left: 40px; top: 36px; width: 40px; height: 40px; }
  .front .wordmark {
    position: absolute; left: 96px; top: 38px;
    font-family: "Anton", "Impact", sans-serif; font-size: 28px; letter-spacing: .5px;
    color: var(--brand-blue); line-height: 1.2;
  }
  .person { position: absolute; left: 40px; top: 104px; }
  .person-name {
    font-family: "Anton", "Impact", sans-serif; font-size: 22px; letter-spacing: 1px;
    color: var(--ink-light); line-height: 1.1;
  }
  .person-role {
    font-family: "Exo 2", sans-serif; font-weight: 600; font-size: 13px; letter-spacing: 1.5px;
    color: var(--brand-blue); margin-top: 2px;
  }
  .company-band {
    position: absolute; left: 0; top: 168px; width: 236px; height: 34px;
    background: var(--brand-blue);
    display: flex; align-items: center; padding-left: 40px;
    font-family: "Exo 2", sans-serif; font-weight: 700; font-size: 15px; letter-spacing: .8px;
    color: var(--ink-dark);
  }
  .contact-list {
    position: absolute; right: 30px; bottom: 26px; list-style: none;
    font-family: "Exo 2", sans-serif; font-size: 12.5px; color: var(--ink-muted);
  }
  .contact-list li {
    display: flex; align-items: center; justify-content: flex-end; gap: 8px; line-height: 20px;
  }
  .contact-icon { width: 13px; height: 13px; fill: var(--brand-blue); }

  /* Back */
  .back { display: flex; flex-direction: column; align-items: center; justify-content: center; gap: 18px; }
  .back .brand-dot { width: 64px; height: 64px; border-width: 4px; }
  .back .wordmark {
    font-family: "Anton", "Impact", sans-serif; font-size: 30px; letter-spacing: .5px;
    color: var(--ink-light);
  }
</style>
</head>
<body>
<main class="canvas">
  <section class="card front" aria-label="Business card front">
    <span class="brand-dot" aria-hidden="true"></span>
    <div class="wordmark">Tolverin Wealth Management</div>
    <div class="person">
      <div class="person-name">MARCUS HALE</div>
      <div class="person-role">MANAGER</div>
    </div>
    <div class="company-band">TOLVERIN EQUITY LLC</div>
    <ul class="contact-list">
      <li>01 482 903
        <svg class="contact-icon" viewBox="0 0 24 24" aria-hidden="true"><path d="M6.6 10.8a15.1 15.1 0 0 0 6.6 6.6l2.2-2.2c.3-.3.7-.4 1-.2 1.1.4 2.3.6 3.6.6.6 0 1 .4 1 1V20c0 .6-.4 1-1 1A17 17 0 0 1 3 4c0-.6.4-1 1-1h3.5c.6 0 1 .4 1 1 0 1.3.2 2.5.6 3.6.1.3 0 .7-.2 1z"/></svg>
      </li>
      <li>hello@tolverinequity.com
        <svg class="contact-icon" viewBox="0 0 24 24" aria-hidden="true"><path d="M2 5h20v14H2z M2 5l10 8 10-8" fill="none" stroke="#1a86d0" stroke-width="2.4"/></svg>
      </li>
      <li>www.tolverinequity.com
        <svg class="contact-icon" viewBox="0 0 24 24" aria-hidden="true"><g fill="none" stroke="#1a86d0" stroke-width="2"><circle cx="12" cy="12" r="10"/><path d="M2 12h20M12 2c3 3 3 17 0 20M12 2c-3 3-3 17 0 20"/></g></svg>
      </li>
    </ul>
  </section>

  <section class="card back" aria-label="Business card back">
    <span class="brand-dot" aria-hidden="true"></span>
    <div class="wordmark">Tolverin Wealth Management</div>
  </section>
</main>
</body>
</html>
```